Redesign of a facility management homepage

We need a redesign/an improved design of the facility management homepage (http://www.krt-lanzfeld.de/).
This websites offers detailed information on the "About us" as company, the "Services" provided and special information on facility and strata management. We would like to keep the structure of the website.
We need ideas/designs how this website could look more modern and confidential and appealing/pleasant for visitors at the same time and not losing the main purpose of information distribution.
The green color must be used since this is the basic color from our logo.
The blue in the background of the logo ist optional. So feel to use it or not.
We need no coding only design (.psd or as .ai)

```html
<!DOCTYPE html>
<html lang="de">
<head>
<meta charset="utf-8">
<title>KRT Büro- und Hausmeisterservice</title>
<link rel="stylesheet" href="https://fonts.googleapis.com/css2?family=Arimo:wght@400;700&display=swap">
<style>
  :root {
    --brand-blue: #053e74;
    --brand-green: #3a9a3c;
    --text-dark: #1a1a1a;
    --text-body: #555;
    --band-grey: #e4e5e7;
    --white: #ffffff;
  }
  * { margin: 0; padding: 0; box-sizing: border-box; }
  html, body { width: 1200px; height: 990px; overflow: hidden; }
  body { font-family: "Arimo", Helvetica, Arial, sans-serif; background: var(--white); position: relative; }

  .site-header { position: absolute; left: 0; top: 0; width: 1200px; height: 181px; background: var(--brand-blue); color: var(--white); }
  .brand { position: absolute; left: 182px; top: 42px; display: flex; align-items: center; gap: 10px; }
  .brand-mark { width: 14px; height: 14px; background: var(--brand-green); }
  .brand-name { font-size: 38px; font-weight: 700; letter-spacing: 1px; color: var(--white); }
  .brand-tagline { position: absolute; left: 182px; top: 106px; font-size: 12px; line-height: 16px; }

  .main-nav { position: absolute; top: 81px; left: 506px; display: flex; gap: 37px; font-size: 14px; }
  .main-nav a { color: var(--white); text-decoration: none; }
  .main-nav a.is-active { font-weight: 700; }
  .nav-chevron { position: absolute; left: 530px; top: 106px; }

  .hero { position: absolute; left: 0; top: 181px; width: 1200px; height: 266px;
    background: linear-gradient(90deg, #8a8a8a 0%, #a49a84 20%, #b7a88b 45%, #8c8a82 65%, #9a9a9a 85%, #a09276 100%); }
  .hero-caption { position: absolute; left: 182px; top: 73px; width: 418px; height: 120px; background: rgba(0,0,0,0.55); color: var(--white); padding: 22px 0 0 22px; }
  .hero-title { font-size: 23px; font-weight: 400; letter-spacing: 0.3px; line-height: 26px; }
  .hero-subtitle { font-size: 16px; font-weight: 700; letter-spacing: 0.6px; line-height: 26px; }
  .hero-tag { font-size: 19px; line-height: 24px; letter-spacing: 0.3px; }
  .hero-dots { position: absolute; left: 576px; top: 232px; display: flex; gap: 6px; }
  .hero-dots span { width: 7px; height: 7px; border-radius: 50%; background: var(--white); }
  .hero-dots span.is-current { background: var(--brand-green); }

  .features { position: absolute; top: 494px; left: 0; width: 1200px; }
  .feature { position: absolute; width: 180px; text-align: center; }
  .feature-icon { width: 75px; height: 75px; margin: 0 auto; background: var(--brand-blue); display: flex; align-items: center; justify-content: center; }
  .feature-title { margin-top: 25px; color: var(--brand-blue); font-size: 17px; font-weight: 400; line-height: 19px; letter-spacing: 0.4px; text-transform: uppercase; }
  .feature-text { margin-top: 10px; color: var(--text-body); font-size: 11px; line-height: 14.5px; }

  .company-band { position: absolute; left: 0; top: 723px; width: 1200px; height: 201px;
    background: linear-gradient(180deg, #e9eaec 0%, #dcdde0 100%); text-align: center; color: var(--text-dark); }
  .company-name { margin-top: 48px; font-size: 16px; font-weight: 700; letter-spacing: 0.8px; }
  .company-address { margin-top: 14px; font-size: 10.5px; line-height: 18.5px; letter-spacing: 0.3px; color: #333; }
  .company-contact { margin-top: 15px; font-size: 10.5px; font-weight: 700; }
  .company-contact .sep { margin: 0 8px; }

  .site-footer { position: absolute; left: 0; top: 924px; width: 1200px; height: 66px; font-size: 10.5px; color: var(--text-dark); }
  .copyright { position: absolute; left: 182px; top: 27px; }
  .footer-nav { position: absolute; right: 180px; top: 27px; display: flex; gap: 29px; }
  .footer-nav a { color: var(--text-dark); text-decoration: none; }
</style>
</head>
<body>

<header class="site-header">
  <div class="brand">
    <span class="brand-mark"></span>
    <span class="brand-name">KRT</span>
  </div>
  <p class="brand-tagline">Büro- und Hausmeisterservice<br>GmbH Lanzfeld Ihr Partner vor Ort.</p>
  <nav class="main-nav">
    <a class="is-active" href="#">Wir über uns</a>
    <a href="#">Gebäudemanagement</a>
    <a href="#">Gebäudeverwaltung</a>
    <a href="#">Vermietung</a>
  </nav>
  <svg class="nav-chevron" width="12" height="8" viewBox="0 0 12 8"><path d="M1 1l5 5 5-5" fill="none" stroke="#fff" stroke-width="2"/></svg>
</header>

<section class="hero" role="img" aria-label="Fotocollage des Fuhrparks: Lieferwagen und Räumfahrzeuge vor einem Gebäude">
  <div class="hero-caption">
    <h1 class="hero-title">UNSER FUHRPARK</h1>
    <p class="hero-subtitle">WINTERDIENST UND SCHNEEBERÄUMUNG</p>
    <p class="hero-tag">KRT VOR ORT</p>
  </div>
  <div class="hero-dots"><span class="is-current"></span><span></span><span></span><span></span></div>
</section>

<section class="features">
  <article class="feature" style="left:195px">
    <div class="feature-icon">
      <svg width="40" height="40" viewBox="0 0 40 40" fill="none" stroke="#fff" stroke-width="2.4" stroke-linecap="round">
        <path d="M10 8c-3 2-4 5-2 10 3 7 8 12 14 15 4 2 7 1 9-2l-4-5-4 2c-3-1-7-5-8-8l2-4-5-5z" fill="#fff" stroke="none"/>
        <path d="M22 12a7 7 0 0 1 6 6M22 7a12 12 0 0 1 11 11M22 2a17 17 0 0 1 16 16"/>
      </svg>
    </div>
    <h2 class="feature-title">Supportstörung<br>online melden</h2>
    <p class="feature-text">Lorem Ipsum is simply dummy text of the printing and typesetting industry.</p>
  </article>
  <article class="feature" style="left:405px">
    <div class="feature-icon">
      <svg width="40" height="28" viewBox="0 0 40 28"><rect x="1" y="1" width="38" height="26" fill="#fff"/><path d="M1 1l19 14L39 1M1 27l14-13M39 27L25 14" fill="none" stroke="#053e74" stroke-width="2"/></svg>
    </div>
    <h2 class="feature-title">Kontakt</h2>
    <p class="feature-text">Lorem Ipsum is simply dummy text of the printing and typesetting industry.</p>
  </article>
  <article class="feature" style="left:616px">
    <div class="feature-icon">
      <svg width="42" height="42" viewBox="0 0 42 42" fill="none" stroke="#fff" stroke-width="2.4">
        <rect x="3" y="6" width="28" height="26"/><path d="M3 13h28M10 2v7M24 2v7"/>
        <path d="M8 18h4M15 18h4M22 18h4M8 24h4M15 24h4" stroke-width="3"/>
        <circle cx="31" cy="31" r="8" fill="#053e74"/><path d="M31 27v4h3"/>
      </svg>
    </div>
    <h2 class="feature-title">Links</h2>
    <p class="feature-text">Lorem Ipsum is simply dummy text of the printing and typesetting industry.</p>
  </article>
  <article class="feature" style="left:826px">
    <div class="feature-icon">
      <svg width="46" height="42" viewBox="0 0 46 42" fill="none" stroke="#fff" stroke-width="2.4" stroke-linejoin="round">
        <path d="M13 18L23 8l10 10M16 15v10h14V15"/><rect x="21" y="18" width="4" height="4" fill="#fff" stroke="none"/>
        <path d="M3 18v10l10 9h8l-7-9M43 18v10l-10 9h-8l7-9"/>
      </svg>
    </div>
    <h2 class="feature-title">Impressum</h2>
    <p class="feature-text">Lorem Ipsum is simply dummy text of the printing and typesetting industry.</p>
  </article>
</section>

<section class="company-band" role="img" aria-label="Blasses Foto von Firmenfahrzeugen als Hintergrund">
  <h2 class="company-name">KRT BÜRO- UND HAUSMEISTERSERVICE GMBH</h2>
  <p class="company-address">MARKTPLATZ 14 IN 04712 LANZFELD VERTRETEN DURCH FRAU SABINE VOHLAND,<br>GESCHÄFTSFÜHRERIN AG DORNSTADT, HR.NR.: HRB 20417</p>
  <p class="company-contact">Tel: 0 34 51 / 72 40 15<span class="sep">•</span> Fax: 0 34 51 / 72 40 16<span class="sep">•</span> Mail: info@krt-lanzfeld.de and Kontaktformular</p>
</section>

<footer class="site-footer">
  <p class="copyright">KRT © 2014 | Privacy Policy</p>
  <nav class="footer-nav">
    <a href="#">Wir über uns</a>
    <a href="#">Gebäudemanagement</a>
    <a href="#">Gebäudeverwaltung</a>
    <a href="#">Vermietung</a>
  </nav>
</footer>

</body>
</html>
```